Wendleby Choir needs a concert poster!

22nd November is Ss Ottoline's Feast, the Patron Saint of music. 100 years ago on that day, Dorian Maltravers was born, famously dubbed the "greatest English composer since Gadsby". 50 years ago that day, three of the most prominent men in history died: this trifecta included theologian and author of 'Quellmark' R. T. Pembury, philosopher and author of 'Silent Tin Harvest' Perrine Vasholt, and one of America's most beloved presidents, Walter G. Ashcombe.

In memory of these prominent figures of the 20th century, the Choir of Holy Ambrose by the Weir Stile (the Market Kirk of Wendleby) perform some of the world's best vocal music composed or inspired by these men. The playlist includes Maltravers's 'Carol for Ss Ottoline', K. D. Ruhnau's 'Geh, Seele, geh', 'The Lantern' by Perrin Vasholt set to music by Miles Tandridge, and Cuthbert Fennimore's 'Lay down, dear one, in quiet rest', written specially for the memorial service of President Walter G Ashcombe in Harrowgate Federal Minster.

We are looking for a dramatic concert poster / or series of posters that encapsulate all these important aspects on this one day. Tickets will be set up on seatpassly.net - space for their logo will be needed.

22nd November 2013, 8pm
Norbury College Chapel, Oxford
Choir of Holy Ambrose by the Weir Stile
Gil Pettifer-Rowe
Tickets: £5

Target Market(s)

Mostly students and staff from the Universities of Wendleby and Marlowe, but also singers from local Oxfordshire choral societies who have a passion for singing and the repertoire. Local musical professionals and appreciators. Not really suitable for children. Cultured adults that support local artistic projects and go to live classical concerts. Higher-end readership. I would like to charge much more for the ticket prices (in order to reflect the quality of the performance) but Oxford is haemorrhaging quality concerts for very little, and the competition is fierce. This poster needs to stand out from the crowd of other events going on, and perhaps be coupled with an inventive marketing strategy.

Industry/Entity Type

Church

Requirements
Must have
• Holy Ambrose by the Weir Stile logo
Seatpassly.net logo

My name prominently displayed

```html
<!DOCTYPE html>
<html lang="en">
<head>
<meta charset="utf-8">
<title>Ss Ottoline's – Concert Poster</title>
<link rel="stylesheet" href="https://fonts.googleapis.com/css2?family=Cinzel:wght@400&family=Noto+Sans:wght@400&display=swap">
<style>
  :root {
    --sky-light: #ecebd8;
    --sky-mid: #bdbc9c;
    --sky-dark: #4c5040;
    --panel: rgba(255, 255, 255, 0.8);
    --ink: #111111;
    --slate: #98a5a4;
    --card-head: #eeeeee;
    --band: #000000;
    --band-text: #ffffff;
    --strip: #ffffff;
  }
  * { margin: 0; padding: 0; box-sizing: border-box; }
  html, body { width: 1200px; height: 1080px; overflow: hidden; background: var(--slate); }
  .poster { position: relative; width: 1200px; height: 1080px; background: var(--slate); font-family: "Noto Sans", sans-serif; color: var(--ink); }

  .hero-photo {
    position: absolute; left: 0; top: 0; width: 1200px; height: 600px;
    background:
      linear-gradient(180deg, rgba(0,0,0,0) 60%, rgba(40,44,32,0.45) 100%),
      radial-gradient(ellipse at 50% 35%, var(--sky-light) 0%, var(--sky-mid) 55%, var(--sky-dark) 100%);
  }

  .info-panel {
    position: absolute; left: 300px; top: 50px; width: 602px; height: 548px;
    background: var(--panel); text-align: center;
  }
  .event-title {
    font-family: "Cinzel", serif; font-weight: 400; font-size: 64px;
    letter-spacing: 2px; margin-top: 40px; line-height: 1.2;
  }
  .event-details { list-style: none; margin-top: 38px; font-size: 32px; line-height: 44px; }
  .album-note { margin-top: 58px; font-size: 17px; line-height: 26px; }

  .tributes { position: absolute; left: 0; top: 619px; width: 1200px; height: 427px; }
  .tribute { position: absolute; top: 0; height: 427px; display: flex; flex-direction: column; }
  .tribute--composer { left: 6px; width: 418px; }
  .tribute--author { left: 461px; width: 382px; }
  .tribute--president { left: 880px; width: 312px; }

  .tribute-name {
    background: var(--card-head); height: 67px; font-weight: 400; font-size: 31px;
    line-height: 64px; padding: 0 8px; white-space: nowrap;
  }
  .tribute--author .tribute-name { text-align: center; line-height: 76px; }
  .tribute--president .tribute-name { text-align: center; font-size: 29px; padding: 0 4px; }
  .tribute-dates {
    background: var(--band); color: var(--band-text); height: 42px; line-height: 42px;
    font-size: 19px; padding: 0 8px;
  }
  .tribute--author .tribute-dates,
  .tribute--president .tribute-dates { text-align: center; }
  .tribute--author .tribute-strip { height: 20px; background: var(--strip); }
  .tribute-portrait { flex: 1; }
  .tribute--composer .tribute-portrait {
    background: radial-gradient(ellipse at 65% 45%, #4a4a4a 0%, #6f6f6f 35%, #b4b4b4 75%, #d2d2d2 100%);
  }
  .tribute--author .tribute-portrait {
    background: radial-gradient(ellipse at 55% 40%, #bdbdbd 0%, #6c6c6c 35%, #2e2e2e 70%, #151515 100%);
  }
  .tribute--president .tribute-portrait {
    background: radial-gradient(ellipse at 50% 45%, #bfbfbf 0%, #8c8c8c 30%, #d9d9d9 60%, #2a2a2a 100%);
  }
</style>
</head>
<body>
<main class="poster">
  <div class="hero-photo" role="img" aria-label="Misty pale sky with silhouetted wild grasses and plants"></div>

  <section class="info-panel">
    <h1 class="event-title">Ss Ottoline's</h1>
    <ul class="event-details">
      <li>22nd November 2013, 8pm</li>
      <li>Norbury College Chapel, Oxford</li>
      <li>Choir of Holy Ambrose by the Weir Stile</li>
      <li>Gil Pettifer-Rowe, director</li>
      <li>Tickets: £5 @ Seatpassly.net</li>
    </ul>
    <p class="album-note">The choir's latest 5 star reviewed<br>CD "The Hollinsworth Legacy"<br>Available now!</p>
  </section>

  <section class="tributes">
    <article class="tribute tribute--composer">
      <h2 class="tribute-name">Dorian Maltravers</h2>
      <p class="tribute-dates">22 Nov 1913 – 4 Dec 1976</p>
      <div class="tribute-portrait" role="img" aria-label="Black and white photograph of the composer seated at a desk with a score"></div>
    </article>
    <article class="tribute tribute--author">
      <h2 class="tribute-name">R. T. Pembury</h2>
      <p class="tribute-dates">29 Nov 1898 – 22 Nov 1963</p>
      <div class="tribute-strip"></div>
      <div class="tribute-portrait" role="img" aria-label="Black and white photograph of the author in spectacles seated in an armchair"></div>
    </article>
    <article class="tribute tribute--president">
      <h2 class="tribute-name">Walter G. Ashcombe</h2>
      <p class="tribute-dates">May 29 1917 – Nov 22 1963</p>
      <div class="tribute-portrait" role="img" aria-label="Black and white head and shoulders photograph of the president in suit and tie"></div>
    </article>
  </section>
</main>
</body>
</html>
```